TBV Risk Management - Blueprint Tally

Upgrade existing PP per the upload. I will use this to email to Prospects and clients as well as posting to our website.
Edit and update pages - this PP was created several years ago and needs a full update based on the same content. Better graphics etc etc are needed
Create some links to websites
TBV Risk Management is a professional consultant where owners have MBA's. Law Degrees and CPCU Designation. PP should be designed with this in mind similar to resources used by CPA's, Accountants or Financial Advisors
Updates
Need extra days to review
Target Market(s)
Construction Contractors
Colors
Designer to choose colors to be used in the design.
Requirements
Must have
- Follow existing PP
Nice to have
- Take a look at our current website which will be upgraded when PP is complete
- www.tbvdeskwork.biz

```html
<!DOCTYPE html>
<html lang="en">
<head>
<meta charset="UTF-8">
<title>Mission Statement</title>
<link rel="stylesheet" href="https://fonts.googleapis.com/css2?family=Play:wght@400;700&display=swap">
<style>
  :root {
    --ink: #333333;
    --ink-dark: #1f1f1f;
    --paper: #ffffff;
    --line: #4a4a4a;
    --skyline-a: #e2e2e2;
  }
  * { box-sizing: border-box; margin: 0; padding: 0; }
  html, body { width: 1200px; height: 675px; overflow: hidden; background: var(--paper); }
  .slide {
    position: relative;
    width: 1200px;
    height: 675px;
    background: var(--paper);
    font-family: "Play", sans-serif;
    color: var(--ink);
    overflow: hidden;
  }
  .skyline-art {
    position: absolute;
    left: 0;
    top: 300px;
    width: 580px;
    height: 375px;
    background: linear-gradient(to right, var(--skyline-a) 0%, rgba(230,230,230,0.7) 55%, rgba(255,255,255,0) 100%);
    -webkit-mask-image: linear-gradient(to bottom, rgba(0,0,0,0), #000 40%);
            mask-image: linear-gradient(to bottom, rgba(0,0,0,0), #000 40%);
  }
  .page-number {
    position: absolute;
    left: 36px;
    top: 34px;
    font-size: 20px;
    color: var(--ink-dark);
  }
  .title-bracket {
    position: absolute;
    left: 104px;
    top: 61px;
  }
  .slide-title {
    position: absolute;
    left: 146px;
    top: 78px;
    font-size: 52px;
    font-weight: 400;
    color: var(--ink);
  }
  .brand {
    position: absolute;
    right: 61px;
    top: 62px;
    text-align: right;
  }
  .brand-name {
    display: flex;
    align-items: center;
    justify-content: flex-end;
    gap: 8px;
    font-size: 23px;
    color: var(--ink-dark);
    line-height: 40px;
  }
  .brand-mark {
    width: 12px;
    height: 12px;
    background: var(--ink-dark);
  }
  .brand-tagline {
    font-size: 9px;
    color: var(--ink-dark);
    margin-top: 2px;
  }
  .mission-list {
    position: absolute;
    left: 146px;
    top: 207px;
    width: 1040px;
    list-style: none;
  }
  .mission-list li {
    font-size: 25px;
    line-height: 30px;
    letter-spacing: 1px;
    color: var(--ink);
    margin-bottom: 30px;
    white-space: nowrap;
  }
</style>
</head>
<body>
<main class="slide">
  <div class="skyline-art" role="img" aria-label="Faint wireframe illustration of high-rise buildings under construction"></div>

  <div class="page-number">2</div>

  <svg class="title-bracket" width="96" height="56" viewBox="0 0 96 56" aria-hidden="true">
    <path d="M1 56 V1 H95" fill="none" stroke="var(--line)" stroke-width="1.5"/>
  </svg>
  <h1 class="slide-title">Mission Statement</h1>

  <div class="brand">
    <div class="brand-name"><span class="brand-mark"></span>Site Ledger</div>
    <div class="brand-tagline">Management Consultants to the Construction Industry</div>
  </div>

  <ul class="mission-list">
    <li>To provide the highest level of personal financial services in a friendly,<br>professional manner</li>
    <li>To encourage contractor clients to establish and extend effective management<br>systems in their companies</li>
    <li>To increase the knowledge and ability of our clients to manage and control their<br>financial well-being</li>
    <li>To provide sound financial/operating&nbsp;&nbsp; management advice in order to maximize<br>clients corporate value while minimizing risk</li>
  </ul>
</main>
</body>
</html>
```